We are full service plumbing contractors that are capable of performing all of your plumbing need...

A clean, crisp website that conveys we can handle any plumbing from drain cleaning, repairs, to new construction. But emphasis on Leak detection, under-slab and underground water service leaks, repairs, and reroutes. Leak detection by acoustical, Thermal, or tracer gas , methods.Also emphasize advanced drain cleaning technologies and equipment. Don't just poke ahole in the drain blockage, Clean the pipe, with our High pressure hydrojetters, or Chain knocker drain cables that expand to the width of the pipe being cleaned.

Number of Pages Required

5+ page

Font styles to use
Sans Serif

Requirements
Should not have
• Canned photos

```html
<!DOCTYPE html>
<html lang="en">
<head>
<meta charset="utf-8">
<title>Flowline Plumbing</title>
<link href="https://fonts.googleapis.com/css2?family=Poppins:wght@400;500;600;700&family=Open+Sans:ital,wght@0,400;0,600;1,400;1,600&display=swap" rel="stylesheet">
<style>
:root{
  --navy:#1c2a63;
  --navy-dark:#141d47;
  --hero-a:#1a3b86;
  --hero-b:#2d5cb8;
  --red:#e1232b;
  --blue:#1f7fd1;
  --ink:#1b1b1b;
  --muted:#7a7a7a;
  --light:#efefef;
  --card:#f2f2f2;
  --dark:#26272c;
  --white:#ffffff;
}
*{box-sizing:border-box;margin:0;padding:0}
html,body{width:1200px;height:4126px;overflow:hidden}
body{font-family:"Open Sans",sans-serif;color:var(--ink);background:var(--white);position:relative}
h1,h2,h3,h4,.btn,.nav,.logo{font-family:"Poppins",sans-serif}
section,header,footer{position:absolute;left:0;width:1200px}
.abs{position:absolute}
.ph{position:absolute}
.btn{position:absolute;display:flex;align-items:center;justify-content:center;color:var(--white);font-size:14px;font-weight:500;border-radius:2px}
.btn.red{background:var(--red)}
.btn.blue{background:var(--blue)}
.rule{display:inline-block;width:60px;height:3px;background:var(--blue);vertical-align:middle;margin-left:14px}

/* hero */
.hero{top:0;height:650px;background:linear-gradient(120deg,var(--hero-a),var(--hero-b) 60%,var(--hero-a));overflow:hidden}
.topbar{position:absolute;top:0;left:0;width:1200px;height:42px;color:var(--white);font-size:13px}
.topbar .addr{position:absolute;left:170px;top:12px;display:flex;gap:8px;align-items:center}
.topbar .call{position:absolute;right:170px;top:11px;font-weight:600;font-size:14px}
.nav{position:absolute;left:160px;top:48px;width:885px;height:70px;background:#0b0b0d;color:var(--white);z-index:3}
.logo{position:absolute;left:26px;top:22px;font-size:18px;font-weight:700;color:var(--red)}
.nav ul{position:absolute;right:70px;top:26px;display:flex;gap:24px;list-style:none;font-size:13px;font-weight:500}
.nav .search{position:absolute;right:24px;top:27px}
.hero h1{position:absolute;left:170px;top:190px;width:560px;color:var(--white);font-size:34px;line-height:54px;font-weight:700;z-index:2}
.worker{left:710px;top:130px;width:330px;height:520px;background:linear-gradient(180deg,#3f6bc0,#1d3470);border-radius:165px 165px 0 0;z-index:1}
.book{position:absolute;right:0;top:220px;width:44px;height:190px;background:var(--red);color:var(--white);writing-mode:vertical-rl;transform:rotate(180deg);display:flex;align-items:center;justify-content:center;font-size:12px;font-weight:600;font-family:"Poppins",sans-serif}
.arrows{position:absolute;left:1045px;top:590px;display:flex;gap:4px;z-index:5}
.arrows span{width:40px;height:42px;background:var(--white);display:flex;align-items:center;justify-content:center}

/* welcome */
.welcome{top:610px;height:520px}
.welcome .intro{position:absolute;left:170px;top:90px;width:410px}
.welcome h2{font-size:23px;font-weight:600;color:var(--ink);white-space:nowrap}
.welcome .rule{width:50px}
.welcome .lead{margin-top:14px;font-size:14px;font-style:italic;font-weight:600;color:#3b3b6a;line-height:22px}
.welcome p.body{margin-top:14px;font-size:12px;color:var(--muted);line-height:20px}
.welcome .emer{margin-top:36px;font-size:17px;font-weight:600;font-family:"Poppins",sans-serif;color:var(--navy)}
.welcome .phone{font-size:30px;font-weight:700;color:var(--red);font-family:"Poppins",sans-serif}
.panel{position:absolute;left:600px;top:0;width:600px;height:520px;background:var(--navy);color:var(--white)}
.feat{position:absolute;left:35px;width:470px;display:flex;gap:30px}
.feat svg{flex:none}
.feat h3{font-size:18px;font-weight:500}
.feat p{margin-top:8px;font-size:12px;line-height:19px;color:#b9c1e0}

/* services */
.services{top:1130px;height:585px;background:var(--light)}
.services h2,.projects h2{position:absolute;left:170px;top:70px;font-size:28px;font-weight:600}
.services .desc{position:absolute;left:170px;top:120px;width:740px;font-size:12px;color:var(--muted);line-height:19px}
.sarrows{position:absolute;left:950px;top:100px;display:flex;gap:8px}
.sarrows span{width:34px;height:34px;background:var(--white);display:flex;align-items:center;justify-content:center}
.card{position:absolute;top:187px;width:205px}
.card .img{height:213px}
.card h4{margin-top:22px;font-size:13px;font-weight:600}

/* experienced */
.experience{top:1715px;height:565px}
.video{left:158px;top:75px;width:367px;height:310px;background:linear-gradient(135deg,#b06a3e,#5e3b27)}
.play{position:absolute;left:158px;top:75px;width:367px;height:310px;display:flex;align-items:center;justify-content:center}
.thumb{top:420px;width:112px;height:70px}
.thumb-play{position:absolute;top:420px;width:112px;height:70px;display:flex;align-items:center;justify-content:center}
.experience .copy{position:absolute;left:607px;top:75px;width:440px}
.experience h2{font-size:24px;line-height:36px;font-weight:600}
.experience .lead{margin-top:18px;font-size:14px;font-style:italic;font-weight:600;color:#3b3b6a;line-height:22px}
.experience p.body{margin-top:14px;font-size:12px;color:var(--muted);line-height:20px}
.ticks{margin-top:28px;list-style:none;font-size:13px}
.ticks li{display:flex;gap:12px;align-items:center;height:30px}

/* projects */
.projects{top:2280px;height:945px;background:var(--dark);color:var(--white)}
.filters{position:absolute;left:170px;top:122px;display:flex;gap:20px;font-size:14px;font-family:"Poppins",sans-serif}
.filters .on{color:var(--red)}
.tile{position:absolute;width:272px}

/* testimonials */
.testimonials{top:3225px;height:480px}
.testimonials h2{position:absolute;left:0;width:1200px;top:90px;text-align:center;font-size:28px;font-weight:600}
.tcard{position:absolute;top:187px;width:425px;height:240px;background:var(--card)}
.tcard .avatar{position:absolute;left:30px;top:40px;width:54px;height:54px;border-radius:50%;background:linear-gradient(135deg,#c7b3a0,#7c6555)}
.tcard h4{position:absolute;left:105px;top:38px;font-size:17px;font-weight:600}
.tcard p{position:absolute;left:105px;top:72px;width:290px;font-size:12px;line-height:20px;color:var(--muted)}
.tcard .q{position:absolute;left:40px;top:115px;color:var(--blue);font-size:48px;font-family:"Poppins",sans-serif;font-weight:700}

/* footer */
.footer{top:3705px;height:361px;background:var(--navy);color:var(--white)}
.footer h3{position:absolute;top:48px;font-size:18px;font-weight:600}
.footer .col{position:absolute;top:105px;font-size:13px;line-height:20px}
.contact li{list-style:none;display:flex;gap:14px;margin-bottom:20px;width:250px}
.social{display:flex;gap:18px;font-weight:700}
.news p{width:250px;color:#cfd4ea}
.input{margin-top:28px;width:270px;height:38px;border-bottom:1px solid #56609a}
.sub{position:relative;margin-top:10px;width:270px;height:40px;background:var(--red);display:flex;align-items:center;justify-content:center;font-weight:600;font-family:"Poppins",sans-serif;font-size:13px}
.map{left:748px;top:95px;width:282px;height:206px;background:linear-gradient(135deg,#e7e4dc,#cfd6c8)}
.bottom{top:4066px;height:60px;background:var(--navy-dark);color:#aab0cc;font-size:12px}
.bottom .copy{position:absolute;left:170px;top:22px}
.bottom .up{position:absolute;left:990px;top:15px;width:34px;height:30px;background:var(--red);display:flex;align-items:center;justify-content:center}
</style>
</head>
<body>

<header class="hero">
  <div class="topbar">
    <div class="addr">
      <svg width="12" height="14" viewBox="0 0 12 14"><path d="M6 0a5 5 0 0 0-5 5c0 4 5 9 5 9s5-5 5-9a5 5 0 0 0-5-5zm0 7a2 2 0 1 1 0-4 2 2 0 0 1 0 4z" fill="#fff"/></svg>
      1224, Venenatis vel pretium ornare.
    </div>
    <div class="call">Call : 0000.000.0000</div>
  </div>
  <nav class="nav">
    <div class="logo">Flowline Plumbing</div>
    <ul><li>Home</li><li>About Us</li><li>Services</li><li>Projects</li><li>Testimonial</li><li>Blog</li><li>Contact Us</li></ul>
    <svg class="search" width="16" height="16" viewBox="0 0 16 16"><circle cx="6.5" cy="6.5" r="5" stroke="#fff" stroke-width="2" fill="none"/><path d="M10.5 10.5L15 15" stroke="#fff" stroke-width="2"/></svg>
  </nav>
  <h1>We can handle any plumbing from drain cleaning, repairs, to new construction</h1>
  <div class="btn red" style="left:170px;top:392px;width:130px;height:44px">Our Services</div>
  <div class="ph worker" role="img" aria-label="Plumber holding a pipe wrench"></div>
  <div class="book">Book Appointment</div>
  <div class="arrows">
    <span><svg width="10" height="12"><path d="M8 1L2 6l6 5" stroke="#333" stroke-width="2" fill="none"/></svg></span>
    <span><svg width="10" height="12"><path d="M2 1l6 5-6 5" stroke="#333" stroke-width="2" fill="none"/></svg></span>
  </div>
</header>

<section class="welcome">
  <div class="intro">
    <h2>Welcome to Flowline Plumbing<span class="rule"></span></h2>
    <p class="lead">Quis autem vel eum iure reprehenderit qui in ea velit esse quam nihil molestiae consequatur vel illum.</p>
    <p class="body">Nemo enim ipsam voluptatem quia voluptas sit aspernatur aut odit aut fugit, sed quia consequuntur magni dolores eos qui ratione voluptatem sequi nesciunt. Neque porro quisquam est, qui dolorem ipsum quia dolor sit amet, consectetur, adipisci velit, sed quia non numquam eius modi tempora incidunt ut labore et dolore magnam aliquam quaerat voluptatem.</p>
    <p class="emer">Any Plumbing Emergency ... Call Us on</p>
    <p class="phone">0000-000-0000</p>
  </div>
  <div class="panel">
    <div class="feat" style="top:90px">
      <svg width="50" height="50" viewBox="0 0 50 50" fill="none" stroke="#fff" stroke-width="2"><circle cx="25" cy="14" r="8"/><path d="M10 44c0-9 7-15 15-15s15 6 15 15"/><path d="M17 8h16"/></svg>
      <div><h3>Experienced Staff</h3><p>Temporibus autem quibusdam et aut officiis debitis aut rerum necessitatibus saepe eveniet ut et voluptates repudiandae sint et molestiae non recusandae.</p></div>
    </div>
    <div class="feat" style="top:220px">
      <svg width="50" height="50" viewBox="0 0 50 50" fill="none" stroke="#fff" stroke-width="2"><path d="M14 8h22l-4 10H18z"/><path d="M25 18v14"/><path d="M18 32h14l-7 12z"/></svg>
      <div><h3>Best Equipments</h3><p>Temporibus autem quibusdam et aut officiis debitis aut rerum necessitatibus saepe eveniet ut et voluptates repudiandae sint et molestiae non recusandae.</p></div>
    </div>
    <div class="feat" style="top:350px">
      <svg width="50" height="50" viewBox="0 0 50 50" fill="none" stroke="#fff" stroke-width="2"><circle cx="25" cy="25" r="18"/><path d="M25 14v11l8 5"/><path d="M5 10l6 4"/></svg>
      <div><h3>24/7 Support</h3><p>Temporibus autem quibusdam et aut officiis debitis aut rerum necessitatibus saepe eveniet ut et voluptates repudiandae sint et molestiae non recusandae.</p></div>
    </div>
  </div>
</section>

<section class="services">
  <h2>Our Services <span class="rule"></span></h2>
  <p class="desc">Neque porro quisquam est qui dolorem ipsum quia dolor sit amet, ut aut reiciendis voluptatibus maiores alias consequatur aut perferendis doloribus asperiores repellat.</p>
  <div class="sarrows">
    <span><svg width="8" height="12"><path d="M7 1L2 6l5 5" stroke="#333" stroke-width="2" fill="none"/></svg></span>
    <span><svg width="8" height="12"><path d="M1 1l5 5-5 5" stroke="#333" stroke-width="2" fill="none"/></svg></span>
  </div>
  <div class="card" style="left:170px"><div class="img" role="img" aria-label="Technician digging to locate an underground leak" style="background:linear-gradient(135deg,#8a5a3a,#c49a6c)"></div><h4>Leak Detection &amp; Repairs</h4></div>
  <div class="card" style="left:390px"><div class="img" role="img" aria-label="Plumber clearing a drain line" style="background:linear-gradient(135deg,#3c7cc4,#d8dde6)"></div><h4>Drain Cleaning &amp; Repairs</h4></div>
  <div class="card" style="left:607px"><div class="img" role="img" aria-label="Plumbing tools and fittings on a work surface" style="background:linear-gradient(135deg,#c23a2f,#e9e1d4)"></div><h4>Plumbing Services</h4></div>
  <div class="card" style="left:825px"><div class="img" role="img" aria-label="Commercial plumbing installation" style="background:linear-gradient(135deg,#6a6a5a,#b8b19c)"></div><h4>Commercial Plumbing</h4></div>
  <div class="btn blue" style="left:528px;top:490px;width:140px;height:42px">View All Services</div>
</section>

<section class="experience">
  <div class="ph video" role="img" aria-label="Video still of a plumber working on a floor drain"></div>
  <div class="play"><svg width="56" height="56"><circle cx="28" cy="28" r="28" fill="#e1232b"/><path d="M22 17l17 11-17 11z" fill="#fff"/></svg></div>
  <div class="ph thumb" style="left:158px;background:linear-gradient(135deg,#7a4b30,#3c2a20)" role="img" aria-label="Video thumbnail"></div>
  <div class="ph thumb" style="left:285px;background:linear-gradient(135deg,#9a6a48,#4a3324)" role="img" aria-label="Video thumbnail"></div>
  <div class="ph thumb" style="left:412px;background:linear-gradient(135deg,#5e5146,#2d2620)" role="img" aria-label="Video thumbnail"></div>
  <div class="thumb-play" style="left:158px"><svg width="24" height="24"><circle cx="12" cy="12" r="12" fill="#e1232b"/><path d="M9 7l8 5-8 5z" fill="#fff"/></svg></div>
  <div class="thumb-play" style="left:285px"><svg width="24" height="24"><circle cx="12" cy="12" r="12" fill="#e1232b"/><path d="M9 7l8 5-8 5z" fill="#fff"/></svg></div>
  <div class="thumb-play" style="left:412px"><svg width="24" height="24"><circle cx="12" cy="12" r="12" fill="#e1232b"/><path d="M9 7l8 5-8 5z" fill="#fff"/></svg></div>
  <div class="copy">
    <h2>Experienced Plumbers Offering<br>Quality Plumbing Services</h2>
    <p class="lead">Quis autem vel eum iure reprehenderit in voluptate velit esse cillum dolore eu fugiat nulla pariatur.</p>
    <p class="body">Neque porro quisquam est, qui dolorem ipsum quia dolor sit amet, consectetur, adipisci velit, sed quia non numquam eius modi tempora incidunt ut labore et dolore magnam aliquam quaerat voluptatem.</p>
    <ul class="ticks">
      <li><svg width="14" height="14"><path d="M2 7l3.5 4L12 3" stroke="#1f7fd1" stroke-width="2.2" fill="none"/></svg>24 Hours Emergency Services</li>
      <li><svg width="14" height="14"><path d="M2 7l3.5 4L12 3" stroke="#1f7fd1" stroke-width="2.2" fill="none"/></svg>Uniformed Licensed Plumbers</li>
      <li><svg width="14" height="14"><path d="M2 7l3.5 4L12 3" stroke="#1f7fd1" stroke-width="2.2" fill="none"/></svg>No Travel Charges</li>
      <li><svg width="14" height="14"><path d="M2 7l3.5 4L12 3" stroke="#1f7fd1" stroke-width="2.2" fill="none"/></svg>Licensed and Insured</li>
      <li><svg width="14" height="14"><path d="M2 7l3.5 4L12 3" stroke="#1f7fd1" stroke-width="2.2" fill="none"/></svg>Free Estimates</li>
    </ul>
  </div>
</section>

<section class="projects">
  <h2>Featured Projects <span class="rule"></span></h2>
  <div class="filters"><span class="on">All</span><span>Plumbing</span><span>Leakages of Pipe</span><span>Drain Cleaning</span><span>Commercial Plumbing</span></div>
  <div class="tile" style="left:170px;top:175px;height:195px;background:linear-gradient(135deg,#4e83c6,#6b4a2f)" role="img" aria-label="Gloved hand holding a pipe fitting over soil"></div>
  <div class="tile" style="left:464px;top:175px;height:195px;background:linear-gradient(135deg,#7d5a3c,#3e6b8e)" role="img" aria-label="Exposed water line in an excavation"></div>
  <div class="tile" style="left:758px;top:175px;height:195px;background:linear-gradient(135deg,#8b6a4a,#c9c4ba)" role="img" aria-label="Plumber working in a trench"></div>
  <div class="tile" style="left:170px;top:392px;height:188px;background:linear-gradient(135deg,#8a6040,#c29a72)" role="img" aria-label="Copper pipe repair in soil"></div>
  <div class="tile" style="left:464px;top:392px;height:188px;background:linear-gradient(135deg,#4a3020,#a7683e)" role="img" aria-label="Copper lines under a slab"></div>
  <div class="tile" style="left:758px;top:392px;height:188px;background:linear-gradient(135deg,#5e7d3a,#8a6a48)" role="img" aria-label="Outdoor pipe excavation"></div>
  <div class="tile" style="left:170px;top:600px;height:183px;background:linear-gradient(135deg,#a9a6a0,#55524e)" role="img" aria-label="Sewer line inspection"></div>
  <div class="tile" style="left:464px;top:600px;height:183px;background:linear-gradient(135deg,#6b6e76,#2f3136)" role="img" aria-label="Water heater installation"></div>
  <div class="tile" style="left:758px;top:600px;height:183px;background:linear-gradient(135deg,#7a5a40,#c7a882)" role="img" aria-label="Pipe section removed from the ground"></div>
  <div class="btn blue" style="left:533px;top:835px;width:134px;height:40px">View All Projects</div>
</section>

<section class="testimonials">
  <h2>Our Testimonials</h2>
  <div class="tcard" style="left:160px">
    <div class="avatar" role="img" aria-label="Client portrait"></div>
    <h4>Evan Hart</h4>
    <p>Excepteur sint occaecat cupidatat non proident, sunt in culpa qui officia deserunt mollit anim id est laborum sed ut perspiciatis unde omnis iste natus error sit voluptatem.</p>
    <div class="q">“</div>
  </div>
  <div class="tcard" style="left:610px">
    <div class="avatar" role="img" aria-label="Client portrait"></div>
    <h4>Lena Brooks</h4>
    <p>Excepteur sint occaecat cupidatat non proident, sunt in culpa qui officia deserunt mollit anim id est laborum sed ut perspiciatis unde omnis iste natus error sit voluptatem.</p>
    <div class="q">“</div>
  </div>
</section>

<footer class="footer">
  <h3 style="left:170px">Contact Us</h3>
  <ul class="col contact" style="left:170px">
    <li><svg width="14" height="16" viewBox="0 0 12 14"><path d="M6 0a5 5 0 0 0-5 5c0 4 5 9 5 9s5-5 5-9a5 5 0 0 0-5-5zm0 7a2 2 0 1 1 0-4 2 2 0 0 1 0 4z" fill="#fff"/></svg><span>1224, Venenatis vel pretium ornare<br>vitae consequat</span></li>
    <li><svg width="14" height="14" viewBox="0 0 14 14"><path d="M3 1l2 3-1.5 1.5a8 8 0 0 0 5 5L10 9l3 2-1 2.5C6 14 0 8 .5 2z" fill="#fff"/></svg><span>0000-000-0000</span></li>
    <li><svg width="14" height="12" viewBox="0 0 14 12"><rect x="1" y="1" width="12" height="10" stroke="#fff" fill="none"/><path d="M1 1l6 5 6-5" stroke="#fff" fill="none"/></svg><span>info@flowlineplumbing.com</span></li>
    <li class="social"><span>f</span><span>G+</span><span>in</span></li>
  </ul>
  <h3 style="left:463px">Newsletter</h3>
  <div class="col news" style="left:463px">
    <p>Subscribe to our Newsletter for latest updates</p>
    <div class="input"></div>
    <div class="sub">SUBSCRIBE</div>
  </div>
  <h3 style="left:748px">Locate Us</h3>
  <div class="ph map" role="img" aria-label="Map showing the office location"></div>
  <svg class="abs" style="left:877px;top:180px" width="24" height="32" viewBox="0 0 12 16"><path d="M6 0a6 6 0 0 0-6 6c0 4.5 6 10 6 10s6-5.5 6-10a6 6 0 0 0-6-6z" fill="#e1232b"/><circle cx="6" cy="6" r="2.2" fill="#fff"/></svg>
</footer>

<section class="bottom">
  <div class="copy">© Copyright All rights reserved. Designed by Flowline</div>
  <div class="up"><svg width="12" height="8"><path d="M1 7l5-5 5 5" stroke="#fff" stroke-width="2" fill="none"/></svg></div>
</section>

</body>
</html>
```